CAR PAINT AEROSOL

car paint aerosol
3 different aerosols
x1 paint
x1 lacquer
x1 primer

We want something eye catching that will outshine competitors this is automotive paint, we are looking for something modern and clean. Will require a logo as well as the can design too. We have added our 'KMV' brand that is already competitive on the market but this looks very 'trade' style so looking for something more retail (will attach photos of our current aerosols) . Please note we are looking for a new brand name, logo and design. So a completely different brand and look to our current KMV aerosols.
examples of competitors attached

label template attached

Target Market(s)

AUTOMOTIVE INDUSTRY TO RETAIL BUYERS,

Industry/Entity Type

car paint

Requirements
Must have
• NEW BRAND NAME , LOGO AND DESIGN
Nice to have
• own domain www.glenvarnish.co.uk not essential to design but would be good for brand to tie in
Should not have
• ideally not red as current brand is

```html
<!DOCTYPE html>
<html lang="en">
<head>
<meta charset="utf-8">
<title>Motorlux Aerosol Range</title>
<link href="https://fonts.googleapis.com/css2?family=Anton&family=Montserrat:wght@700&family=Roboto:wght@500&display=swap" rel="stylesheet">
<style>
  :root {
    --bg-top: #e2e2e2;
    --bg-bottom: #c8c8c8;
    --cap: #141414;
    --cap-edge: #2c2c2c;
    --label-top: #141516;
    --label-low: #26292b;
    --ring: #f2f2f2;
    --logo-ink: #d6d6d6;
    --silver-1: #ffffff;
    --silver-2: #8c8c8c;
    --blue-1: #38d0f4;
    --blue-2: #2a3cb0;
    --green-1: #a8f23c;
    --green-2: #3f9a18;
  }
  * { margin: 0; padding: 0; box-sizing: border-box; }
  html, body { width: 1200px; height: 912px; overflow: hidden; }
  body {
    background: linear-gradient(180deg, var(--bg-top), var(--bg-bottom));
    font-family: "Montserrat", sans-serif;
    position: relative;
  }
  .range { position: absolute; inset: 0; }

  .can { position: absolute; }
  .can--paint   { left: 366px; top: 124px; width: 148px; --accent-1: var(--silver-1); --accent-2: var(--silver-2); z-index: 1; }
  .can--lacquer { left: 696px; top: 124px; width: 148px; --accent-1: var(--green-1); --accent-2: var(--green-2); z-index: 1; }
  .can--primer  { left: 512px; top: 71px;  width: 184px; --accent-1: var(--blue-1);  --accent-2: var(--blue-2);  z-index: 2; }

  .can__cap {
    height: 161px;
    background: linear-gradient(90deg, var(--cap-edge), var(--cap) 25%, var(--cap) 75%, var(--cap-edge));
    border-radius: 12px 12px 0 0;
  }
  .can--primer .can__cap { height: 184px; }
  .can__ring { height: 4px; background: var(--ring); }

  .can__label {
    position: relative;
    height: 453px;
    background: linear-gradient(180deg, var(--label-top) 45%, var(--label-low));
    border-top: 3px solid var(--accent-1);
    border-bottom: 3px solid var(--accent-1);
  }
  .can--primer .can__label { height: 532px; border-top-color: var(--accent-2); border-bottom-color: var(--accent-2); }
  .can__base { height: 6px; background: var(--ring); border-radius: 0 0 6px 6px; }

  .brand {
    position: absolute;
    left: 0; right: 0;
    top: 26px;
    text-align: center;
    font-weight: 700;
    font-size: 27px;
    line-height: 0.95;
    letter-spacing: 0.5px;
    color: var(--logo-ink);
  }
  .can--primer .brand { top: 30px; font-size: 31px; }

  .product-name { position: absolute; overflow: visible; }
  .product-name text { font-family: "Anton", sans-serif; }
  .can--paint .product-name   { left: 30px; top: 98px; }
  .can--primer .product-name  { left: 40px; top: 121px; }
  .can--lacquer .product-name { left: 34px; top: 104px; }

  .color-tag {
    position: absolute;
    left: 30px; top: 346px;
    width: 88px; height: 48px;
    background: linear-gradient(90deg, #f4f4f4, #b9b9b9);
    font-family: "Roboto", sans-serif;
    font-weight: 500;
    font-size: 15px;
    color: #2a2a2a;
    display: flex; align-items: center; justify-content: center;
  }

  .volume {
    position: absolute;
    bottom: 0; left: 50%;
    transform: translateX(-50%);
    width: 56px; height: 20px;
    border-radius: 5px 5px 0 0;
    font-family: "Roboto", sans-serif;
    font-weight: 500;
    font-size: 12px;
    display: flex; align-items: center; justify-content: center;
  }
  .can--paint .volume   { background: #f2f2f2; color: #222; }
  .can--lacquer .volume { background: linear-gradient(90deg, var(--green-1), var(--green-2)); color: #1a1a1a; }
  .can--primer .volume  { width: 68px; height: 26px; font-size: 15px; background: linear-gradient(90deg, var(--blue-1), #2f7de0); color: #fff; }
</style>
</head>
<body>
  <main class="range">
    <section class="can can--paint">
      <div class="can__cap"></div>
      <div class="can__ring"></div>
      <div class="can__label">
        <div class="brand">MOTOR<br>LUX</div>
        <svg class="product-name" width="88" height="226" viewBox="0 0 88 226" aria-label="Paint">
          <defs>
            <linearGradient id="paint-fill" gradientUnits="userSpaceOnUse" x1="0" y1="0" x2="226" y2="0">
              <stop offset="0" stop-color="#7a7a7a"/>
              <stop offset="0.35" stop-color="#ffffff"/>
              <stop offset="0.7" stop-color="#d8d8d8"/>
              <stop offset="1" stop-color="#8a8a8a"/>
            </linearGradient>
          </defs>
          <text transform="translate(88 226) rotate(-90)" font-size="102" textLength="226" lengthAdjust="spacingAndGlyphs" fill="url(#paint-fill)">PAINT</text>
        </svg>
        <div class="color-tag">COLOR</div>
        <div class="volume">400ml</div>
      </div>
      <div class="can__base"></div>
    </section>

    <section class="can can--primer">
      <div class="can__cap"></div>
      <div class="can__ring"></div>
      <div class="can__label">
        <div class="brand">MOTOR<br>LUX</div>
        <svg class="product-name" width="105" height="348" viewBox="0 0 105 348" aria-label="Primer">
          <defs>
            <linearGradient id="primer-fill" gradientUnits="userSpaceOnUse" x1="0" y1="0" x2="348" y2="0">
              <stop offset="0" stop-color="#2a3cb0"/>
              <stop offset="0.55" stop-color="#2f8fe0"/>
              <stop offset="1" stop-color="#38d0f4"/>
            </linearGradient>
          </defs>
          <text transform="translate(105 348) rotate(-90)" font-size="122" textLength="348" lengthAdjust="spacingAndGlyphs" fill="url(#primer-fill)">PRIMER</text>
        </svg>
        <div class="volume">400ml</div>
      </div>
      <div class="can__base"></div>
    </section>

    <section class="can can--lacquer">
      <div class="can__cap"></div>
      <div class="can__ring"></div>
      <div class="can__label">
        <div class="brand">MOTOR<br>LUX</div>
        <svg class="product-name" width="79" height="290" viewBox="0 0 79 290" aria-label="Lacquer">
          <defs>
            <linearGradient id="lacquer-fill" gradientUnits="userSpaceOnUse" x1="0" y1="0" x2="290" y2="0">
              <stop offset="0" stop-color="#3f9a18"/>
              <stop offset="0.6" stop-color="#7fd52c"/>
              <stop offset="1" stop-color="#a8f23c"/>
            </linearGradient>
          </defs>
          <text transform="translate(79 290) rotate(-90)" font-size="92" textLength="290" lengthAdjust="spacingAndGlyphs" fill="url(#lacquer-fill)">LACQUER</text>
        </svg>
        <div class="volume">400ml</div>
      </div>
      <div class="can__base"></div>
    </section>
  </main>
</body>
</html>
```